Business Cards for Communications Technology Company

We are an innovative software company based in Tropical North Queensland, Australia. We have several brands with a focus on communications software for businesses. We are looking for a business card that is very innovate and creative whilst still remaining professional on a corporate level.

Our internal culture is very progressive and expresses a blend between the clarity of our natural surroundings and the highly technological industry we work in. Our current branding blends a modern minimalist typeface with the desire to push the boundaries in the way we communicate.

This is a corporate level business card for the communications software industry and may possibly also encompass our brands MarNetwork, PelFax, TukMailer and our B2B marketing service—with our companies name being Viresca Partners. Showing other brands on the business card is optional not compulsory.

Technical notes:

-We will attach all logo's and some examples of our corporate branding
- Would be willing to print with various papers, embossed, metallic ink, curved edges etc. in a standard business card size

Sample content:

Rowan Pellick
Senior Account Manager
Phone: 1300 842 916 / +617 4583 2764
Email: r.pellick@viresca.com.au
Web: www.viresca.com.au

Sincerely,
Viresca Partners.

```html
<!DOCTYPE html>
<html lang="en">
<head>
<meta charset="utf-8">
<title>Viresca Partners Business Card</title>
<link rel="stylesheet" href="https://fonts.googleapis.com/css2?family=Open+Sans:wght@400;600;700&display=swap">
<style>
  :root {
    --backdrop: #3a3532;
    --card: #141414;
    --card-edge: #0c0c0c;
    --white: #f4f4f4;
    --green: #5e9e3c;
    --emboss: #262626;
    --emboss-text: #4a4a4a;
    --muted: #8a8a8a;
  }
  html, body {
    margin: 0;
    width: 1200px;
    height: 864px;
    overflow: hidden;
    background: var(--backdrop);
    font-family: "Open Sans", Arial, sans-serif;
  }
  .canvas {
    position: relative;
    width: 1200px;
    height: 864px;
  }
  .card {
    position: absolute;
    background: var(--card);
    border-radius: 4px;
    box-shadow: 0 10px 30px rgba(0,0,0,.45);
  }
  .card-back {
    left: 80px;
    top: 90px;
    width: 560px;
    height: 320px;
    display: flex;
    flex-direction: column;
    align-items: center;
    justify-content: center;
  }
  .back-mark {
    display: flex;
    align-items: center;
    gap: 16px;
  }
  .back-mark .dot {
    width: 84px;
    height: 84px;
    border-radius: 50%;
    background: var(--emboss);
  }
  .back-mark .name {
    font-size: 40px;
    font-weight: 400;
    letter-spacing: 2px;
    color: var(--emboss-text);
  }
  .back-web {
    margin-top: 34px;
    font-size: 14px;
    letter-spacing: 6px;
    color: var(--muted);
  }
  .card-front {
    left: 560px;
    top: 430px;
    width: 580px;
    height: 331px;
  }
  .brand {
    position: absolute;
    left: 120px;
    top: 70px;
    display: flex;
    align-items: center;
    gap: 14px;
  }
  .brand .dot {
    width: 54px;
    height: 54px;
    border-radius: 50%;
    background: var(--white);
  }
  .brand .name {
    font-size: 56px;
    font-weight: 400;
    color: var(--white);
    letter-spacing: 1px;
    line-height: 1;
  }
  .person {
    position: absolute;
    right: 335px;
    top: 195px;
    text-align: right;
  }
  .person .full-name {
    font-size: 15px;
    font-weight: 700;
    color: var(--green);
    text-transform: uppercase;
    letter-spacing: .5px;
  }
  .person .role {
    font-size: 14px;
    color: var(--white);
  }
  .divider {
    position: absolute;
    left: 260px;
    top: 192px;
    width: 1px;
    height: 88px;
    background: var(--white);
    opacity: .8;
  }
  .contacts {
    position: absolute;
    left: 278px;
    top: 194px;
    margin: 0;
    padding: 0;
    list-style: none;
    font-size: 14px;
    line-height: 21px;
    color: var(--white);
  }
  .contacts li {
    display: flex;
    align-items: center;
    gap: 9px;
  }
  .contacts svg {
    width: 11px;
    height: 11px;
    fill: var(--green);
    flex: none;
  }
</style>
</head>
<body>
<div class="canvas">
  <section class="card card-back">
    <div class="back-mark">
      <span class="dot"></span>
      <span class="name">VIRESCA</span>
    </div>
    <div class="back-web">www.viresca.com.au</div>
  </section>

  <section class="card card-front">
    <div class="brand">
      <span class="dot"></span>
      <span class="name">VIRESCA</span>
    </div>
    <div class="person">
      <div class="full-name">Rowan Pellick</div>
      <div class="role">Senior Account Manager</div>
    </div>
    <div class="divider"></div>
    <ul class="contacts">
      <li><svg viewBox="0 0 12 12"><path d="M2 1h2l1 3-1.5 1a7 7 0 0 0 3.5 3.5L8 7l3 1v2a1 1 0 0 1-1 1A9 9 0 0 1 1 2a1 1 0 0 1 1-1z"/></svg>1300 842 916</li>
      <li><svg viewBox="0 0 12 12"><path d="M2 1h2l1 3-1.5 1a7 7 0 0 0 3.5 3.5L8 7l3 1v2a1 1 0 0 1-1 1A9 9 0 0 1 1 2a1 1 0 0 1 1-1z"/></svg>+617 4583 2764</li>
      <li><svg viewBox="0 0 12 12"><path d="M1 2.5h10v7H1zM1 3l5 3.5L11 3v1L6 7.5 1 4z"/></svg>r.pellick@viresca.com.au</li>
      <li><svg viewBox="0 0 12 12"><circle cx="6" cy="6" r="5.5"/></svg>www.viresca.com.au</li>
    </ul>
  </section>
</div>
</body>
</html>
```